Political sign design, fonts colors and layout

I am running for Town Council.

My message is done, and *a draft is attached* with the text we wish to use. It says "Elect Dana Velloway" etc. In Maroon and White. I am not a designer, but this is somewhat close to what we are looking for.

I need help with colors and fonts, layout, spacing, and general cleanup.

I'm attaching the town high school logo:

- "B" for Brockmere: with black and white outlines on the fonts
- we want to incorporate the black and white on the fonts
- for the entire text, parts of the text, or best would be a mix

This is for signs printed and placed all over my town.

We need two versions

1. square, 4' by 4' version
2. 36" by 24" version

The smaller version will drop the three bullet pointed text, but otherwise can be identical.

The sign can only use 3 printed colors (due to printing costs.)

1. maroon,
2. white,
3. black.

The maroon should match the maroon from the high school logo attached, which I believe I did in the draft.

We also like the white border around the outside, like in the "scoreboard" design attached.

Thanks for your attention, wish me luck.

Dana

Target Market(s)

SIgns, Political market

Industry/Entity Type

Political

Font styles to use
Sans Serif
Other font styles liked:
• Arial Black, Sans Serif Bold

Requirements
Must have
• maroon background, white font.
• - black borders around fonts where appropriate
• - great spacing
• - great typeface usage
• - clean and crisp political sign, visible while driving.
• - my name "Dana Velloway" much larger like the draft, or the appropriate additional size
• - two versions, one square, and one 36" / 24"
Nice to have
• - nice borders
• - dress it up a bit, using italics and bold fonts, without making it flashy or busy.
Should not have
• Must be easily readable from a car, except for "Paid for by Friends of Dana Velloway" which can be tiny.
• Colors are noted in the description, the "Brockmere Maroon" as the background, white font, and some use of black.

```html
<!DOCTYPE html>
<html lang="en">
<head>
<meta charset="utf-8">
<title>Elect Dana Velloway – Yard Sign</title>
<link rel="stylesheet" href="https://fonts.googleapis.com/css2?family=Montserrat:wght@400;500;700;800;900&family=Oswald:wght@700&display=swap">
<style>
  :root {
    --maroon: #731f35;
    --white: #ffffff;
    --black: #000000;
  }
  html, body {
    margin: 0;
    padding: 0;
    width: 1200px;
    height: 800px;
    overflow: hidden;
    background: var(--maroon);
  }
  .sign { display: block; width: 1200px; height: 800px; }
  .sign-bg { fill: var(--maroon); }
  .frame-outer { fill: none; stroke: var(--white); stroke-width: 5; }
  .frame-inner { fill: none; stroke: var(--white); stroke-width: 2; }
  .header-panel { fill: var(--white); stroke: var(--black); stroke-width: 3; }
  .office-band { fill: var(--black); }
  .star-black { fill: var(--black); }
  .star-white { fill: var(--white); }
  .star-maroon { fill: var(--black); }
  .slogan-top {
    font-family: "Montserrat", sans-serif; font-weight: 800; font-size: 30px;
    fill: var(--black);
  }
  .elect {
    font-family: "Montserrat", sans-serif; font-weight: 400; font-size: 103px;
    fill: var(--black);
  }
  .candidate-name {
    font-family: "Montserrat", sans-serif; font-weight: 900; font-size: 132px;
    paint-order: stroke fill; stroke-linejoin: round;
  }
  .candidate-name.outer { fill: var(--black); stroke: var(--black); stroke-width: 16; }
  .candidate-name.inner { fill: var(--maroon); stroke: var(--white); stroke-width: 8; }
  .office {
    font-family: "Montserrat", sans-serif; font-weight: 700; font-size: 30px;
    letter-spacing: 2px; fill: var(--white);
  }
  .tagline {
    font-family: "Montserrat", sans-serif; font-size: 54px; fill: var(--white);
  }
  .tagline.shadow { fill: var(--black); }
  .tagline .strong { font-weight: 800; }
  .tagline .light { font-weight: 400; }
  .web {
    font-family: "Montserrat", sans-serif; font-weight: 400; font-size: 48px;
    fill: var(--white);
  }
  .issues-strip { fill: var(--white); }
  .issue {
    font-family: "Oswald", sans-serif; font-weight: 700; font-size: 40px;
    fill: var(--maroon);
  }
  .vote {
    font-family: "Montserrat", sans-serif; font-weight: 900; font-size: 90px;
    paint-order: stroke fill; stroke-linejoin: round;
  }
  .vote.shadow { fill: var(--black); stroke: var(--black); stroke-width: 10; }
  .vote.face { fill: var(--white); stroke: var(--black); stroke-width: 6; }
  .vote-sup { font-size: 44px; }
  .disclaimer {
    font-family: "Montserrat", sans-serif; font-weight: 400; font-size: 19px;
    fill: var(--white);
  }
</style>
</head>
<body>
<svg class="sign" viewBox="0 0 1200 800" xmlns="http://www.w3.org/2000/svg">
  <defs>
    <path id="star" d="M50 0 L61 35 L98 35 L68 57 L79 91 L50 70 L21 91 L32 57 L2 35 L39 35 Z"/>
  </defs>

  <rect class="sign-bg" x="0" y="0" width="1200" height="800"/>

  <!-- border frame -->
  <rect class="frame-outer" x="20" y="20" width="1160" height="760" rx="6"/>
  <rect class="frame-inner" x="30" y="30" width="1140" height="740" rx="4"/>

  <!-- header panel -->
  <path class="header-panel" d="M76 52 H1123 A28 28 0 0 0 1151 80 V302 A28 28 0 0 0 1123 330 H76 A28 28 0 0 0 48 302 V80 A28 28 0 0 0 76 52 Z"/>
  <text class="slogan-top" x="600" y="97" text-anchor="middle">Take back our town!</text>

  <g class="star-black">
    <use href="#star" transform="translate(129 104) scale(0.85)"/>
    <use href="#star" transform="translate(224 104) scale(0.85)"/>
    <use href="#star" transform="translate(319 104) scale(0.85)"/>
    <use href="#star" transform="translate(789 104) scale(0.85)"/>
    <use href="#star" transform="translate(884 104) scale(0.85)"/>
    <use href="#star" transform="translate(979 104) scale(0.85)"/>
  </g>
  <text class="elect" x="435" y="193" textLength="334" lengthAdjust="spacingAndGlyphs">ELECT</text>

  <text class="candidate-name outer" x="109" y="311" textLength="982" lengthAdjust="spacingAndGlyphs">DANA VELLOWAY</text>
  <text class="candidate-name inner" x="109" y="311" textLength="982" lengthAdjust="spacingAndGlyphs">DANA VELLOWAY</text>

  <!-- office band -->
  <rect class="office-band" x="91" y="330" width="1016" height="51"/>
  <text class="office" x="600" y="367" text-anchor="middle">FOR BROCKMERE COUNCILMAN / TRUSTEE</text>

  <!-- tagline -->
  <text class="tagline shadow" x="603" y="448" text-anchor="middle"><tspan class="strong">Fighting</tspan><tspan class="light"> for </tspan><tspan class="strong">Brockmere</tspan></text>
  <text class="tagline" x="600" y="445" text-anchor="middle"><tspan class="strong">Fighting</tspan><tspan class="light"> for </tspan><tspan class="strong">Brockmere</tspan></text>

  <!-- web line -->
  <g class="star-white">
    <use href="#star" transform="translate(241 481) scale(0.33)"/>
    <use href="#star" transform="translate(280 481) scale(0.33)"/>
    <use href="#star" transform="translate(319 481) scale(0.33)"/>
    <use href="#star" transform="translate(838 481) scale(0.33)"/>
    <use href="#star" transform="translate(877 481) scale(0.33)"/>
    <use href="#star" transform="translate(916 481) scale(0.33)"/>
  </g>
  <text class="web" x="600" y="511" text-anchor="middle">www.taxfair.com</text>

  <!-- issues strip -->
  <rect class="issues-strip" x="44" y="531" width="1111" height="77" rx="6"/>
  <text class="issue" x="59" y="584" textLength="215" lengthAdjust="spacingAndGlyphs">STOP HIGH TAXES</text>
  <use class="star-maroon" href="#star" transform="translate(283 556) scale(0.29)"/>
  <text class="issue" x="320" y="584" textLength="360" lengthAdjust="spacingAndGlyphs">CLEAN UP OUR GOVERNMENT</text>
  <use class="star-maroon" href="#star" transform="translate(688 556) scale(0.29)"/>
  <text class="issue" x="724" y="584" textLength="409" lengthAdjust="spacingAndGlyphs">PRESERVE OUR NEIGHBORHOODS</text>

  <!-- vote line -->
  <g transform="translate(5 5)">
    <text class="vote shadow" x="121" y="703" textLength="523" lengthAdjust="spacingAndGlyphs">VOTE NOV. 8</text>
    <text class="vote shadow vote-sup" x="648" y="676" textLength="44" lengthAdjust="spacingAndGlyphs">th</text>
    <text class="vote shadow" x="712" y="703" textLength="342" lengthAdjust="spacingAndGlyphs">"ROW A"</text>
  </g>
  <text class="vote face" x="121" y="703" textLength="523" lengthAdjust="spacingAndGlyphs">VOTE NOV. 8</text>
  <text class="vote face vote-sup" x="648" y="676" textLength="44" lengthAdjust="spacingAndGlyphs">th</text>
  <text class="vote face" x="712" y="703" textLength="342" lengthAdjust="spacingAndGlyphs">"ROW A"</text>

  <text class="disclaimer" x="600" y="742" text-anchor="middle">Paid for by Friends of Dana</text>
</svg>
</body>
</html>
```